Ad-Services Website

The project is for an agency which provides a 360 service around the world of printing and advertising. Without much focus on the advertising per say, but much more focus on the medium on which advertisement can be achieved, such as banners, moving banners, boards and so on.

Futhermore more the company deals with material printing so it has advertising agencies as clients.

Finally it represents several companies in Greece for materials around advertising such as stands, ad-walls, banners and so on.

The webpage needs to have web 2.0 look an feel, and it will lack in content, therefore the focus should not be in large sections of text.

I can have a pdf sent with a small presentation that was done to the client, and the structure to which he agreed to

The following website has the look & feel of what we are looking for

http://www.loriku.gr

The companies current website where you can get the colors and logos from is

http://tamperoadv.gr
Updates

Hello,

Thank you all very much for your designs, we really appreciate your contribution.

Maybe in our next project we can work together.

Best Regards,
Marek

Industry/Entity Type

Advertising

```html
<!DOCTYPE html>
<html lang="en">
<head>
<meta charset="utf-8">
<title>Tampero Advertising</title>
<link href="https://fonts.googleapis.com/css2?family=Arimo:wght@400;700&family=Oswald:wght@400;500&display=swap" rel="stylesheet">
<style>
  :root {
    --sage: #d2dcc0;
    --sage-dark: #c4d1b1;
    --paper: #fbfdf5;
    --slate: #3d5a6c;
    --slate-deep: #2b4451;
    --footer: #41606f;
    --card: #b7c6bd;
    --ink: #555a58;
    --ink-soft: #8aa0a8;
    --divider: #8c8f8a;
  }
  * { box-sizing: border-box; margin: 0; padding: 0; }
  html, body { width: 798px; height: 1200px; overflow: hidden; background: #ffffff; }
  body { font-family: "Arimo", Arial, sans-serif; color: var(--ink); position: relative; }

  .page {
    position: absolute; left: 12px; top: 12px; width: 775px; height: 1173px;
    background: var(--paper); box-shadow: 0 0 6px rgba(0,0,0,.35); overflow: hidden;
  }

  /* header */
  .site-header { position: absolute; left: 0; top: 0; width: 100%; height: 131px; background: var(--sage); box-shadow: 0 2px 3px rgba(0,0,0,.2); }
  .brand { position: absolute; left: 15px; top: 42px; font-family: "Arimo", Arial, sans-serif; font-weight: 700; font-size: 30px; color: #ffffff; letter-spacing: -0.5px; }
  .brand-mark { display: inline-block; width: 14px; height: 14px; border-radius: 50%; background: var(--slate); margin-right: 6px; vertical-align: 3px; }
  .search { position: absolute; left: 573px; top: 20px; width: 160px; height: 25px; background: #fff; border: 1px solid #c9cfbf; font-size: 11px; color: #b8bcb4; padding: 6px 10px; }
  .search-icon { position: absolute; left: 740px; top: 18px; }
  .main-nav { position: absolute; top: 70px; left: 0; width: 100%; height: 60px; }
  .nav-item { position: absolute; width: 110px; margin-left: -55px; text-align: center; }
  .nav-item svg { display: block; margin: 0 auto; height: 30px; }
  .nav-label { font-family: "Oswald", sans-serif; font-size: 16px; color: #2e3a3a; margin-top: 5px; letter-spacing: .2px; }

  /* intro */
  .intro-title { position: absolute; left: 15px; top: 193px; width: 283px; height: 117px; background: var(--sage); font-weight: 700; font-size: 25px; line-height: 31px; color: #5e615c; text-align: center; padding-top: 10px; }
  .specs-heading { position: absolute; left: 15px; top: 324px; font-size: 20px; font-weight: 700; color: var(--slate); }
  .specs-text { position: absolute; left: 15px; top: 360px; width: 283px; font-size: 9px; line-height: 17.7px; text-align: justify; color: #5a5a5a; }

  /* slider */
  .slider { position: absolute; left: 336px; top: 194px; width: 427px; height: 323px; background: #2a2220; box-shadow: 0 0 2px rgba(0,0,0,.5); }
  .slide-photo { position: absolute; left: 8px; top: 8px; right: 8px; bottom: 0; background: radial-gradient(circle at 48% 45%, #6a5e8a 0, #2a2b3d 18%, #6b4f3b 40%, #a27d5c 62%, #3b2a22 100%); }
  .caption { position: absolute; left: 0; right: 0; bottom: 0; height: 81px; background: rgba(40,40,45,.78); padding: 6px 16px; color: #e5e5e5; }
  .caption h3 { font-size: 12px; font-weight: 700; margin-bottom: 3px; }
  .caption p { font-size: 9px; line-height: 17.7px; text-align: justify; }
  .thumbs { position: absolute; left: 336px; top: 529px; width: 427px; height: 65px; }
  .thumb { position: absolute; top: 0; width: 97px; height: 65px; border: 3px solid #6e6e6a; }
  .thumb:nth-child(1) { left: 0; background: radial-gradient(circle at 45% 50%, #7a6ba0 0, #222 25%, #8a6a4e 55%, #3b2a22 100%); }
  .thumb:nth-child(2) { left: 111px; background: linear-gradient(160deg, #f4c9be, #e9a8a0 60%, #d8867c); }
  .thumb:nth-child(3) { left: 220px; background: linear-gradient(90deg, #1d4fc4 0, #1e4fd2 70%, #e6ecf5 100%); }
  .thumb:nth-child(4) { left: 329px; background: linear-gradient(160deg, #c9d5dd, #7f8f99 50%, #dfe6ea); }

  /* category strip */
  .category-strip { position: absolute; left: 14px; top: 657px; width: 749px; height: 64px; background: var(--sage); display: flex; }
  .strip-arrow { flex: 0 0 13px; height: 64px; background: var(--divider); display: flex; align-items: center; justify-content: center; }
  .strip-item { flex: 0 0 177px; height: 64px; display: flex; align-items: center; justify-content: center; gap: 8px; font-family: "Oswald", sans-serif; font-size: 17px; color: #3c4a48; letter-spacing: -.4px; white-space: nowrap; }
  .strip-divider { flex: 0 0 5px; height: 64px; background: var(--divider); }
  .section-mark { font-family: "Arimo", sans-serif; font-size: 27px; line-height: 1; }

  /* feature cards */
  .feature { position: absolute; top: 787px; width: 242px; height: 167px; background: var(--card); border-radius: 3px; box-shadow: 0 2px 3px rgba(0,0,0,.35); text-align: center; }
  .feature h2 { font-size: 14px; font-weight: 400; color: var(--slate); margin-top: 12px; }
  .feature svg { display: block; margin: 10px auto 0; }

  /* footer */
  .site-footer { position: absolute; left: 0; top: 1018px; width: 100%; height: 130px; background: var(--footer); }
  .footer-col { position: absolute; top: 14px; }
  .footer-col h4 { font-size: 11px; font-weight: 700; color: #ffffff; margin-bottom: 16px; }
  .footer-col li { list-style: none; font-size: 9px; font-weight: 700; color: var(--ink-soft); line-height: 20px; }
  .footer-bar { position: absolute; left: 0; top: 1148px; width: 100%; height: 25px; background: var(--slate-deep); color: #b8c6cc; font-size: 9px; font-weight: 700; text-align: center; line-height: 25px; }
  .social { position: absolute; top: 4px; width: 17px; height: 17px; border-radius: 50%; background: #6d8794; }
</style>
</head>
<body>
<div class="page">

  <header class="site-header">
    <div class="brand"><span class="brand-mark"></span>Tampero</div>
    <div class="search">Search</div>
    <svg class="search-icon" width="22" height="30" viewBox="0 0 22 30">
      <circle cx="10" cy="10" r="7" fill="none" stroke="#7d9b9a" stroke-width="3"/>
      <line x1="13" y1="16" x2="18" y2="27" stroke="#7d9b9a" stroke-width="4" stroke-linecap="round"/>
    </svg>
    <nav class="main-nav">
      <div class="nav-item" style="left:292px">
        <svg viewBox="0 0 34 30" width="34"><g stroke="#6d8a8c" stroke-width="2" fill="none"><circle cx="17" cy="15" r="3"/><circle cx="5" cy="6" r="3"/><circle cx="29" cy="6" r="3"/><circle cx="6" cy="26" r="3"/><circle cx="28" cy="25" r="3"/><circle cx="17" cy="3" r="2"/><path d="M8 8 14 13M26 8 20 13M8 24 14 17M26 23 20 17M17 5 17 12"/></g></svg>
        <div class="nav-label">BRANDS</div>
      </div>
      <div class="nav-item" style="left:393px">
        <svg viewBox="0 0 32 32" width="32"><g fill="#7d9c98"><circle cx="16" cy="16" r="6"/><circle cx="16" cy="5" r="5"/><circle cx="16" cy="27" r="5"/><circle cx="5" cy="16" r="5"/><circle cx="27" cy="16" r="5"/><circle cx="8" cy="8" r="4"/><circle cx="24" cy="8" r="4"/><circle cx="8" cy="24" r="4"/><circle cx="24" cy="24" r="4"/></g></svg>
        <div class="nav-label">PRINTING</div>
      </div>
      <div class="nav-item" style="left:500px">
        <svg viewBox="0 0 34 30" width="34"><rect x="1" y="1" width="32" height="24" fill="#8fb0b0" stroke="#3d5a6c" stroke-width="2"/><rect x="13" y="25" width="8" height="4" fill="#3d5a6c"/></svg>
        <div class="nav-label">DISPLAYS</div>
      </div>
      <div class="nav-item" style="left:619px">
        <svg viewBox="0 0 44 30" width="44"><rect x="2" y="10" width="8" height="10" fill="#3d5a6c"/><polygon points="10,10 40,2 40,28 10,20" fill="#8fb0b0"/><rect x="40" y="2" width="3" height="26" fill="#3d5a6c"/></svg>
        <div class="nav-label">ADVERTISING</div>
      </div>
      <div class="nav-item" style="left:734px">
        <svg viewBox="0 0 32 32" width="32"><circle cx="16" cy="16" r="16" fill="#3d5a6c"/><circle cx="16" cy="12" r="5" fill="#8fb0b0"/><rect x="8" y="19" width="16" height="7" rx="3" fill="#8fb0b0"/></svg>
        <div class="nav-label">ABOUT US</div>
      </div>
    </nav>
  </header>

  <h1 class="intro-title">Tampero<br>Printing and<br>AdvertisingLTD.</h1>
  <h2 class="specs-heading">Specs »</h2>
  <p class="specs-text">Lorem ipsum dolor sit amet, consectetuer adipiscing elit, sed diam nonummy nibh euismod tincidunt ut laoreet dolore magna aliquam erat volutpat. Ut wisi enim ad minim veniam, quis nostrud exerci tation ullamcorper suscipit lobortis nisl ut aliquip ex ea commodo consequat. Duis autem vel eum iriure dolor in hendrerit in vulputate velit esse molestie consequat, vel illum dolore eu feugiat nulla facilisis at vero eros et accumsan et iusto odio dignissim qui blandit praesent luptatum zzril delenit augue duis dolore te feugait nulla facilisi. Nam liber tempor cum soluta nobis eleifend option congue nihil imperdiet doming id quod mazim placerat facer possim assum. Typi non habent claritatem insitam; est usus legentis in</p>

  <section class="slider">
    <div class="slide-photo" role="img" aria-label="Photo of a hand holding a camera lens reflecting a colourful scene"></div>
    <div class="caption">
      <h3>Caption</h3>
      <p>tation ullamcorper suscipit lobortis nisl ut aliquip ex ea commodo consequat. Duis autem vel eum iriure dolor in hendrerit in vulputate velit esse molestie consequat, vel illum dolore eu feugiat nulla facilisis at vero eros et accumsan et iusto</p>
    </div>
  </section>
  <div class="thumbs">
    <div class="thumb" role="img" aria-label="Thumbnail: camera lens in hand"></div>
    <div class="thumb" role="img" aria-label="Thumbnail: pink printed poster lettering"></div>
    <div class="thumb" role="img" aria-label="Thumbnail: blue painted texture"></div>
    <div class="thumb" role="img" aria-label="Thumbnail: soft grey feather texture"></div>
  </div>

  <section class="category-strip">
    <div class="strip-arrow"><svg width="8" height="10"><polygon points="7,0 7,10 0,5" fill="#fff"/></svg></div>
    <div class="strip-item">PRINT LARGE COMPANY</div>
    <div class="strip-divider"></div>
    <div class="strip-item">
      <svg width="18" height="16" viewBox="0 0 18 16"><g fill="none" stroke="#3c4a48" stroke-width="2"><rect x="5" y="4" width="8" height="8"/><circle cx="3" cy="3" r="2"/><circle cx="15" cy="3" r="2"/><circle cx="3" cy="13" r="2"/><circle cx="15" cy="13" r="2"/></g></svg>U PRINTING NOM</div>
    <div class="strip-divider"></div>
    <div class="strip-item"><span class="section-mark">§</span>APSLOM COLORS</div>
    <div class="strip-divider"></div>
    <div class="strip-item"><svg width="22" height="22" viewBox="0 0 22 22"><circle cx="11" cy="11" r="9.5" fill="none" stroke="#3c4a48" stroke-width="2"/><circle cx="11" cy="11" r="2.5" fill="#3c4a48"/></svg>FILL MARKETING</div>
    <div class="strip-arrow"><svg width="8" height="10"><polygon points="0,0 0,10 7,5" fill="#fff"/></svg></div>
  </section>

  <section class="feature" style="left:15px">
    <h2>Services</h2>
    <svg width="150" height="110" viewBox="0 0 150 110">
      <g fill="#3d5a6c">
        <circle cx="72" cy="65" r="28"/><g stroke="#3d5a6c" stroke-width="9" stroke-dasharray="8 7.2"><circle cx="72" cy="65" r="33" fill="none"/></g>
        <circle cx="22" cy="28" r="14"/><g stroke="#3d5a6c" stroke-width="6" stroke-dasharray="5 4.4"><circle cx="22" cy="28" r="17" fill="none"/></g>
        <circle cx="124" cy="22" r="16"/><g stroke="#3d5a6c" stroke-width="7" stroke-dasharray="6 5.5"><circle cx="124" cy="22" r="20" fill="none"/></g>
      </g>
      <circle cx="72" cy="65" r="12" fill="#b7c6bd"/><circle cx="22" cy="28" r="6" fill="#b7c6bd"/><circle cx="124" cy="22" r="7" fill="#b7c6bd"/>
    </svg>
  </section>
  <section class="feature" style="left:268px">
    <h2>Our Partners</h2>
    <svg width="150" height="110" viewBox="0 0 150 110">
      <g fill="#4b6b7c"><circle cx="100" cy="28" r="22"/><path d="M62 100 Q66 62 100 62 Q134 62 138 100 Z"/></g>
      <g fill="#3d5a6c"><circle cx="55" cy="34" r="24"/><path d="M10 110 Q14 68 55 68 Q96 68 100 110 Z"/></g>
    </svg>
  </section>
  <section class="feature" style="left:521px">
    <h2>What We Do</h2>
    <svg width="120" height="110" viewBox="0 0 120 110">
      <g stroke="#3d5a6c" stroke-linecap="round" fill="none">
        <line x1="30" y1="95" x2="90" y2="30" stroke-width="16"/>
        <line x1="30" y1="30" x2="88" y2="95" stroke-width="12"/>
      </g>
      <circle cx="90" cy="25" r="20" fill="#3d5a6c"/><rect x="86" y="4" width="14" height="16" fill="#b7c6bd" transform="rotate(40 93 12)"/>
      <rect x="15" y="14" width="24" height="18" rx="4" fill="#3d5a6c" transform="rotate(45 27 23)"/>
    </svg>
  </section>

  <footer class="site-footer">
    <div class="footer-col" style="left:15px"><h4>ABOUT US</h4><ul><li>Tampero</li><li>advertising</li><li>and Printing LTD.</li></ul></div>
    <div class="footer-col" style="left:132px"><h4>ADVERTISING</h4><ul><li>Roff Lorum</li><li>Texture Ipsum</li><li>Kinder Lines</li><li>Way Wing Lin</li></ul></div>
    <div class="footer-col" style="left:258px"><h4>DISPLAY</h4><ul><li>Paper Lalpic</li><li>Texture Surface</li><li>Dotted Lines</li><li>Dinamic piece</li></ul></div>
    <div class="footer-col" style="left:383px"><h4>PRINTING</h4><ul><li>Ligh Sink Ink</li><li>Ringer Ink</li><li>Roller Mask</li><li>Pinger Nash</li></ul></div>
    <div class="footer-col" style="left:508px"><h4>BRAND</h4><ul><li>Ringer Ink</li><li>X Printing</li><li>Cool Paper</li><li>Texture Diamond</li></ul></div>
    <div class="footer-col" style="left:635px"><h4>CONTACT US</h4><ul><li>555-014-2290</li><li>admin@tampero.example</li></ul></div>
  </footer>
  <div class="footer-bar">© Copyright 2012 Tampero Advertising and Printing LTD.
    <span class="social" style="left:680px"></span><span class="social" style="left:701px"></span>
  </div>

</div>
</body>
</html>
```